Illustration Design Project

I am looking for a 'how it works' banner type illustration to go at the top of my website which I can place into a wordpress site. This will be to explain how the website works, in three easy pictures with a label below.
The website is www.zelPrang.co.uk (please see contruction page to give you inspiration and colours)

The word description (Label below picture) on the site shall be:

How it works:

zelPrang! + Your Inspiration = A Happy face

or

Your Inspiration + zelPrang! = A Happy face

The pictures above the label shall be:

zelPrang! - the picture above this shall be the zelPrang! logo from my site

Your inspiration - shall be a picture of a person with an idea type light bulb effect, please look at logo and design around the style of the logo.

A Happy faces - shall be a smiley face in the same style as the 'your inspiration' face

Other comments:

The zelPrang logo will be the logo uploaded without the .co.uk

The face's must be explosive, creative but simple in structure.

Target Market(s)

16 - 30

Requirements
Must have
• Must be in the same style as the logo zelPrang.co.uk

```html
<!DOCTYPE html>
<html lang="en">
<head>
<meta charset="utf-8">
<title>How it works – zelPrang!</title>
<link rel="stylesheet" href="https://fonts.googleapis.com/css2?family=Luckiest+Guy&family=Mulish:wght@700&display=block">
<style>
  :root {
    --page-bg: #ececec;
    --banner-core: #5cc9ff;
    --banner-mid: #2f7dff;
    --banner-edge: #0030ff;
    --title-top: #fff23a;
    --title-bottom: #f07a10;
    --title-outline: #ffffff;
    --title-shadow: #0a0a14;
    --label: #ffffff;
    --art-warm: #f3c9b6;
    --art-deep: #8a5a3c;
    --art-glow: #fff3a0;
    --brand-accent: #5ed0ff;
  }
  * { margin: 0; padding: 0; box-sizing: border-box; }
  html, body {
    width: 1200px; height: 849px; overflow: hidden;
    background: var(--page-bg);
  }
  .banner {
    position: absolute; left: 0; top: 86px;
    width: 1200px; height: 677px;
    background: radial-gradient(ellipse 58% 62% at 50% 47%, var(--banner-core) 0%, var(--banner-mid) 42%, var(--banner-edge) 88%);
    overflow: hidden;
  }
  .banner-title {
    position: absolute; left: 0; top: 0;
    width: 1200px; height: 677px;
  }
  .banner-title text {
    font-family: "Luckiest Guy", cursive;
    font-size: 150px;
  }
  .title-shadow { fill: var(--title-shadow); stroke: var(--title-shadow); stroke-width: 16px; stroke-linejoin: round; }
  .title-face { fill: url(#titleFill); stroke: var(--title-outline); stroke-width: 12px; stroke-linejoin: round; paint-order: stroke fill; }

  .step-art { position: absolute; }
  .brand-mark {
    left: 270px; top: 370px; width: 168px; height: 96px;
    display: flex; align-items: center; justify-content: center; gap: 8px;
    font-family: "Mulish", sans-serif; font-weight: 700; font-size: 26px;
    color: var(--label); white-space: nowrap;
  }
  .brand-dot { width: 14px; height: 14px; border-radius: 50%; background: var(--brand-accent); flex: none; }
  .inspiration-art {
    left: 519px; top: 375px; width: 135px; height: 115px;
    border-radius: 10px;
    background: radial-gradient(circle at 80% 22%, var(--art-glow) 0%, var(--art-warm) 38%, var(--art-deep) 120%);
    opacity: 0.85;
  }
  .happy-art {
    left: 791px; top: 375px; width: 99px; height: 115px;
    border-radius: 10px;
    background: radial-gradient(circle at 50% 60%, var(--art-warm) 0%, var(--art-warm) 35%, var(--art-deep) 120%);
    opacity: 0.85;
  }

  .step-labels {
    position: absolute; left: 0; top: 509px; width: 1200px; height: 30px;
    font-family: "Mulish", sans-serif; font-weight: 700; font-size: 20px;
    letter-spacing: 1.2px; color: var(--label);
  }
  .step-labels span { position: absolute; transform: translateX(-50%); white-space: nowrap; }
</style>
</head>
<body>
  <main class="banner">
    <svg class="banner-title" viewBox="0 0 1200 677" aria-label="How it works">
      <defs>
        <linearGradient id="titleFill" x1="0" y1="0" x2="0" y2="1">
          <stop offset="0.25" stop-color="var(--title-top)"/>
          <stop offset="1" stop-color="var(--title-bottom)"/>
        </linearGradient>
      </defs>
      <text class="title-shadow" x="197" y="285" textLength="820" lengthAdjust="spacingAndGlyphs" aria-hidden="true">HOW IT WORKS</text>
      <text class="title-face" x="190" y="275" textLength="820" lengthAdjust="spacingAndGlyphs">HOW IT WORKS</text>
    </svg>

    <div class="step-art brand-mark"><span class="brand-dot"></span>zelPrang</div>
    <div class="step-art inspiration-art" role="img" aria-label="Cartoon character with an idea light bulb"></div>
    <div class="step-art happy-art" role="img" aria-label="Cartoon character with a big happy grin"></div>

    <div class="step-labels">
      <span style="left:354px">zelPrang!</span>
      <span style="left:450px">+</span>
      <span style="left:585px">Your Inspiration</span>
      <span style="left:717px">=</span>
      <span style="left:843px">A Happy face</span>
    </div>
  </main>
</body>
</html>
```